■依頼の目的/概要
・スーパーの店頭でチーズケーキを販売促進させるためのポスターを作成希望です。前回もクラフタス上で募集しており、今回第2弾の募集となります。
・前回は「月間●本売れた伝説のチーズケーキ」というコピーで作って頂いております(参考までに既存販促ポスター添付しておきます)。今回小売店様から別の販促ポスターを求められており、再度お願いするものです。

■依頼詳細
・ポスター内に貼付のチーズケーキ画像を入れてください。
(写真を使う場合も4つ全て使っていただく必要はありません)
・商品名の「濃厚シルクレアチーズケーキ」「濃厚ほろ蜜チーズケーキ」を入れてください。
・今回は下のセールスコピーのうち、1つもしくは複数を使用し、セールスコピーにあったテイストのデザインにして頂きたいです。なお、下記セールスコピーは全てクラフタス内でお願いし、考えて頂いたものです。
・良いデザインのものがあれば複数当選させたいと思っています。

①専門店にはもう行けない。
⇒スイーツ専門店並みのクオリティの商品ながら価格は半額近く。 コスパが良すぎて、これを買ってしまったら専門店には行けないという趣旨のコピーです。

②このチーズ感、もはや牧場
⇒チーズ生地にクリームチーズを69%配合している濃厚なチーズケーキであるということをコミカルに表現したコピーです。牛の写真やイラストを入れたり、コミカルでパンチのあるポスターにしてもらえたらと思っています。

③濃いから、恋した。
⇒濃厚なチーズケーキに恋をした、という「濃い」と「恋い」をかけたコピーです。お洒落で女性ウケしそうな、しっとりとしたデザインにしたいです。

④売り切れちゃうから、つぶやかないで。
⇒クオリティが高くてコスパが良い商品なので、SNS等で発信しないで!という趣旨のコピーです。

⑤買って後悔。2個買っておけばよかったと。
⇒あえてネガティブなワードを先頭に持ってくることで目を引くようにしたコピーです。

⑥濃くて美味しい、手頃で嬉しい。
⇒商品の良さを語呂よくシンプルに表したコピーです。

その他何かご不明な点がございましたら、お気軽にご質問下さい。
よろしくお願いいたします。
ご提案ありがとうございます。

ごちゃごちゃしたスーパーの売場の中で目を引かせるためには
コピーのインパクトが重要なのかなと思っております。

添付資料としている「伝説のチーズケーキ」のように、
ある程度セールスコピーを大きく目立たせるポスターのほうが好ましいです。

「このチーズ感、もはや牧場」
牛のインパクト、セールスコピーの力強さが売り場で目を引くつくりになっており、
気に入りました。

「もうひとつ買っておけばよかった」
漫画調のデザインが販促ポスターとしては斬新で気に入りました。

「濃いから、恋した」
全体のバランスのよさ、色使いが気にいりました。

数多くのご提案を頂きありがとうございました。

引き続き新商品の販促資料や商品パッケージ等を
クラフタ上で募集してまいりますので、引き続きよろしくお願いいたします。

```html
<!DOCTYPE html>
<html lang="ja">
<head>
<meta charset="utf-8">
<title>このチーズ感、もはや牧場</title>
<link rel="stylesheet" href="https://fonts.googleapis.com/css2?family=Dela+Gothic+One&family=M+PLUS+1p:wght@800&display=swap">
<style>
  :root {
    --paper: #ffffff;
    --ink: #111111;
    --sky: #5fb4e4;
    --sky-deep: #2f86c4;
    --ribbon-start: #e2307f;
    --ribbon-end: #a82a8e;
    --cake-dark: #9a5520;
    --cake-mid: #d38a35;
    --cake-light: #f4b73f;
    --cake-pale: #f8cf6a;
  }
  html, body { margin: 0; padding: 0; overflow: hidden; background: var(--paper); }
  .poster {
    position: relative;
    width: 847px;
    height: 1200px;
    overflow: hidden;
    background: var(--paper);
  }
  .pasture {
    position: absolute;
    left: 0; top: 205px;
    width: 847px; height: 815px;
    background:
      radial-gradient(ellipse at 30% 30%, rgba(255,255,255,0.28) 0%, rgba(255,255,255,0) 55%),
      radial-gradient(ellipse at 75% 60%, rgba(255,255,255,0.22) 0%, rgba(255,255,255,0) 50%),
      linear-gradient(160deg, var(--sky) 0%, var(--sky-deep) 100%);
  }
  .product-photo {
    position: absolute;
    left: 140px; top: 560px;
    width: 720px; height: 470px;
    border-radius: 18px 18px 0 0;
    background:
      linear-gradient(180deg, rgba(255,255,255,0.18) 0%, rgba(255,255,255,0) 25%),
      linear-gradient(90deg, var(--cake-dark) 0%, var(--cake-mid) 38%, var(--cake-light) 58%, var(--cake-pale) 100%);
    box-shadow: 0 0 30px rgba(0,0,0,0.25);
  }
  .band {
    position: absolute;
    left: 0; width: 847px;
    background: var(--paper);
  }
  .band--top { top: 0; height: 205px; }
  .band--bottom { top: 1020px; height: 180px; }
  .headline {
    position: absolute;
    left: 0; width: 847px;
    margin: 0;
    font-family: "Dela Gothic One", sans-serif;
    font-weight: 400;
    color: var(--ink);
    text-align: center;
    line-height: 1;
    white-space: nowrap;
  }
  .headline--top { top: 40px; font-size: 122px; letter-spacing: -4px; }
  .headline--bottom { top: 1040px; font-size: 148px; letter-spacing: 2px; }
  .ribbon { position: absolute; left: 0; }
  .ribbon svg { display: block; }
  .ribbon__label {
    position: absolute;
    left: 22px; top: 0;
    margin: 0;
    height: 100%;
    display: flex;
    flex-direction: column;
    justify-content: center;
    font-family: "M PLUS 1p", sans-serif;
    font-weight: 800;
    color: var(--paper);
    font-size: 32px;
    line-height: 1.22;
    white-space: nowrap;
  }
  .ribbon--first { top: 282px; }
  .ribbon--second { top: 494px; }
  .bubble {
    position: absolute;
    left: 500px; top: 410px;
    width: 270px; height: 190px;
  }
  .bubble svg { position: absolute; left: 0; top: 0; display: block; }
  .bubble__text {
    position: absolute;
    left: 0; top: 32px;
    width: 270px;
    margin: 0;
    text-align: center;
    font-family: "M PLUS 1p", sans-serif;
    font-weight: 800;
    color: var(--ink);
    font-size: 38px;
    line-height: 1.3;
  }
</style>
</head>
<body>
<main class="poster">
  <div class="pasture" role="img" aria-label="水色の地に白い牛の群れが並ぶイラスト模様"></div>

  <div class="product-photo" role="img" aria-label="濃厚シルクレアチーズケーキと濃厚ほろ蜜チーズケーキを並べたパッケージ写真"></div>

  <div class="band band--top"></div>
  <h1 class="headline headline--top">このチーズ感、</h1>

  <div class="ribbon ribbon--first">
    <svg width="355" height="112" viewBox="0 0 355 112" aria-hidden="true">
      <defs>
        <linearGradient id="ribbonFill" x1="0" y1="0" x2="1" y2="1">
          <stop offset="0" stop-color="#e2307f"/>
          <stop offset="1" stop-color="#a82a8e"/>
        </linearGradient>
      </defs>
      <polygon points="0,0 355,0 318,56 355,112 0,112" fill="url(#ribbonFill)"/>
    </svg>
    <p class="ribbon__label"><span>濃厚シルクレア</span><span>チーズケーキ</span></p>
  </div>

  <div class="ribbon ribbon--second">
    <svg width="355" height="112" viewBox="0 0 355 112" aria-hidden="true">
      <polygon points="0,0 355,0 318,56 355,112 0,112" fill="url(#ribbonFill)"/>
    </svg>
    <p class="ribbon__label"><span>濃厚ほろ蜜</span><span>チーズケーキ</span></p>
  </div>

  <div class="bubble">
    <svg width="270" height="190" viewBox="0 0 270 190" aria-hidden="true">
      <path d="M135 8 C210 8 262 42 262 86 C262 130 210 160 135 160 C120 160 106 159 94 157 L66 186 L70 150 C32 137 8 114 8 86 C8 42 60 8 135 8 Z" fill="var(--paper)" stroke="#333" stroke-width="3"/>
    </svg>
    <p class="bubble__text">モ〜ウ、<br>さいこう</p>
  </div>

  <div class="band band--bottom"></div>
  <p class="headline headline--bottom">もはや牧場</p>
</main>
</body>
</html>
```